Australian tool shop needs a label designed for a new product

we need a label designed for a new product (Trowel Mate) but since its new to the market we want the label to be based on the design of the top 2 existing brands so it is instantly familiar with the customer, attached a photo of the 2 different brands that it needs to look like

Target Market(s)

BRICKLAYERS/ BUILDERS

Industry/Entity Type

Building Product

Requirements
Must have
• MUST HAVE SIMULAR FEELS AS THE UPLOADED IMAGE AND FEEL FAMILIAR WITH THOSE BRANDS

```html
<!DOCTYPE html>
<html lang="en">
<head>
<meta charset="utf-8">
<title>Trowel Mate Label</title>
<link rel="stylesheet" href="https://fonts.googleapis.com/css2?family=Bebas+Neue&family=Oswald:wght@400;500&display=swap">
<style>
  :root {
    --page: #efefef;
    --label: #f7f7f7;
    --orange: #dc7f1f;
    --charcoal: #1e2a31;
    --slate: #2c3c44;
    --white: #ffffff;
    --ink: #1b1b1b;
  }
  html, body {
    margin: 0;
    padding: 0;
    width: 1200px;
    height: 1131px;
    overflow: hidden;
    background: var(--page);
  }
  .label {
    position: absolute;
    left: 170px;
    top: 25px;
    width: 860px;
    height: 1080px;
    background: var(--label);
    box-shadow: 0 2px 10px rgba(0,0,0,0.08);
    overflow: hidden;
  }
  .product-name {
    position: absolute;
    left: 118px;
    top: 51px;
    margin: 0;
    font-family: "Bebas Neue", sans-serif;
    font-weight: 400;
    font-size: 228px;
    line-height: 200px;
    color: var(--orange);
    letter-spacing: 1px;
  }
  .product-blurb {
    position: absolute;
    left: 120px;
    top: 440px;
    width: 320px;
    margin: 0;
    font-family: "Oswald", sans-serif;
    font-size: 19px;
    line-height: 25px;
    color: var(--ink);
  }
  .tool-art {
    position: absolute;
    left: 470px;
    top: 450px;
    width: 290px;
    height: 215px;
    border-radius: 14px;
    background: linear-gradient(150deg, #dc7f1f 0%, #e9a25a 35%, #3a4d57 70%, #2c3c44 100%);
  }
  .rule {
    position: absolute;
    left: 0;
    top: 680px;
    width: 860px;
    height: 11px;
    background: var(--slate);
  }
  .weight-band {
    position: absolute;
    left: 0;
    top: 704px;
    width: 860px;
    height: 132px;
    background: var(--charcoal);
  }
  .net-weight {
    position: absolute;
    right: 90px;
    top: 26px;
    margin: 0;
    font-family: "Oswald", sans-serif;
    font-weight: 500;
    font-size: 80px;
    line-height: 80px;
    color: var(--white);
    letter-spacing: -1px;
  }
  .safety-band {
    position: absolute;
    left: 0;
    top: 856px;
    width: 860px;
    height: 224px;
    background: var(--orange);
  }
  .safety-icons {
    position: absolute;
    left: 108px;
    top: 54px;
  }
  .batch-box {
    position: absolute;
    left: 620px;
    top: 72px;
    width: 178px;
    height: 102px;
    background: var(--white);
    border: 2px solid var(--charcoal);
    box-sizing: border-box;
  }
</style>
</head>
<body>
  <main class="label">
    <h1 class="product-name">Trowel<br>Mate</h1>
    <p class="product-blurb">Ready-mixed lime for mortar and render, easy to spread, smooth finish, ideal for brickwork and blockwork</p>

    <div class="tool-art" role="img" aria-label="Illustration of a bricklaying trowel with an orange handle"></div>

    <div class="rule"></div>
    <section class="weight-band">
      <p class="net-weight">20kg</p>
    </section>

    <section class="safety-band">
      <svg class="safety-icons" width="400" height="128" viewBox="0 0 400 128" role="img" aria-label="Safety icons: wear a respirator, wear gloves, wear safety boots">
        <g fill="none" stroke="#1e2a31" stroke-width="5">
          <circle cx="58" cy="64" r="56"/>
          <circle cx="198" cy="64" r="56"/>
          <circle cx="338" cy="64" r="56"/>
        </g>
      </svg>
      <div class="batch-box"></div>
    </section>
  </main>
</body>
</html>
```